Christmas social media advert post

I am looking for an eye catching advert for use mainly on social media posts.
The following is the detail of the event.

Christmas special offer-
£10pp,– offer includes –
Half an hour Toboggan track,
Half an hour Slingshot paintballs (20 paintballs pp) and safe target archery (under cover and indoor ranges). Activities all the family from age 4 to grandparents can join in,
Also available – Add on indoor activities including Mini Curling, Bead Blitz, Safe axe throwing, Air juggler – from £3.50pp and age 6plus
Café open for hot food and drinks in the ‘Fireside Frost Lodge and the heated Christmas marquee.

A basic idea I put together for what I feel is the important information is -

Christmas Special offer -
Starts Saturday 20th December.
£10pp – offer includes –
Half an hour Slingshot paintballs (20 paintballs pp) and safe target archery (under cover and indoor ranges). Activities all the family from age 4 to grandparents can join in. Booking is essential - details on how below.
Also available Add on indoor activities - including Mini Curling, Bead Blitz, Safe axe throwing, Air juggler – from £3.50pp and age 6plus.
Ages start from 4 plus.
All activities are great for children and adults so perfect for families as well as friends, parties and get togethers.
Free huge car parks,
Booking is easy-
Just Message from messenger (on this post) or email
martin@hollowbrookleisurepark.co.uk for availability of your preferred date and time.

I would be happy to send the detailed information to enquiries if it meant a better looking advert / post.

Full details are in the picture uploads, feel free to use as much or as little of the information as you feel best.

```html
<!DOCTYPE html>
<html lang="en">
<head>
<meta charset="utf-8">
<title>Christmas Special Offer</title>
<link rel="stylesheet" href="https://fonts.googleapis.com/css2?family=Libre+Caslon+Text:wght@400;700&family=Lobster&family=Playfair+Display:wght@800;900&display=block">
<style>
  :root {
    --wood-dark: #3b2a1f;
    --wood-mid: #6b5140;
    --wood-light: #8a6d56;
    --pine: #2b4527;
    --pine-light: #4d6b3c;
    --paper: #efeae4;
    --paper-shade: #d6ccc1;
    --snow: #fbfaf8;
    --title-green: #3f5c2a;
    --red: #c0161f;
    --deep-red: #9a1a1d;
    --band: #8c1515;
    --ink: #161412;
    --white: #ffffff;
  }
  * { margin: 0; padding: 0; box-sizing: border-box; }
  html, body { width: 960px; height: 1200px; overflow: hidden; background: var(--wood-dark); }
  .poster {
    position: relative; width: 960px; height: 1200px; overflow: hidden;
    font-family: "Libre Caslon Text", Georgia, serif; color: var(--ink);
  }
  .backdrop {
    position: absolute; inset: 0;
    background:
      radial-gradient(circle at 4% 8%, var(--pine-light) 0, var(--pine) 70px, transparent 150px),
      radial-gradient(circle at 96% 14%, var(--pine-light) 0, var(--pine) 80px, transparent 170px),
      radial-gradient(circle at 2% 60%, var(--pine) 0, transparent 120px),
      radial-gradient(circle at 98% 55%, var(--pine) 0, transparent 90px),
      linear-gradient(90deg, #4a3627 0%, var(--wood-mid) 10%, var(--wood-light) 50%, var(--wood-mid) 90%, #4a3627 100%);
  }
  .header-board {
    position: absolute; left: 82px; top: 14px; width: 770px; height: 226px;
    background: linear-gradient(180deg, #8a6d56 0%, #6e5442 55%, #5a4333 100%);
    border-top: 10px solid var(--snow);
    border-bottom: 10px solid var(--snow);
    box-shadow: 0 6px 12px rgba(0,0,0,.35);
  }
  .title-main {
    position: absolute; left: 0; width: 960px; top: 34px; text-align: center;
    font-family: "Playfair Display", Georgia, serif; font-weight: 900; font-size: 84px; line-height: 1;
    color: var(--title-green); letter-spacing: -2px;
    -webkit-text-stroke: 1px #1f3114;
    text-shadow: 2px 2px 0 var(--white), -1px -1px 0 var(--white), 0 5px 8px rgba(0,0,0,.55);
  }
  .title-script {
    position: absolute; left: 0; width: 960px; top: 118px; text-align: center;
    font-family: "Lobster", "Brush Script MT", cursive; font-weight: 400; font-size: 84px; line-height: 1;
    color: var(--red); transform: rotate(-3deg);
    text-shadow: 2px 2px 0 var(--white), -2px -2px 0 var(--white), 2px -2px 0 var(--white), -2px 2px 0 var(--white), 0 6px 8px rgba(0,0,0,.5);
  }
  .paper {
    position: absolute;
    background: radial-gradient(ellipse at center, var(--paper) 50%, var(--paper-shade) 100%);
    border-top: 10px solid var(--snow);
    box-shadow: 0 4px 10px rgba(0,0,0,.3);
  }
  .offer-panel { left: 102px; top: 236px; width: 756px; height: 308px; }
  .line { position: absolute; left: 0; width: 100%; text-align: center; white-space: nowrap; }
  .script { font-family: "Lobster", "Brush Script MT", cursive; font-weight: 400; color: var(--deep-red); }
  .script sup { font-size: 45%; vertical-align: 0.9em; }
  .red { color: var(--deep-red); font-weight: 700; }
  .bold { font-weight: 700; }
  .starts { top: 30px; font-size: 27px; font-weight: 700; }
  .starts .script { font-size: 40px; }
  .price { top: 84px; font-size: 24px; }
  .price .amount { font-size: 38px; font-weight: 700; }
  .inc-1 { top: 124px; font-size: 22px; font-weight: 700; }
  .inc-2 { top: 159px; font-size: 22px; font-weight: 700; }
  .inc-3 { top: 193px; font-size: 22px; font-weight: 700; }
  .inc-4 { top: 225px; font-size: 20px; }
  .essential { top: 250px; font-size: 34px; }
  .photo { position: absolute; border: 6px solid var(--snow); box-shadow: 0 4px 10px rgba(0,0,0,.35); }
  .photo-toboggan {
    left: 58px; top: 552px; width: 413px; height: 258px;
    background:
      radial-gradient(ellipse at 28% 62%, #c8393a 0, rgba(200,57,58,.6) 40px, transparent 90px),
      radial-gradient(ellipse at 70% 70%, #f4f4f2 0, #dadcd8 140px, transparent 260px),
      linear-gradient(175deg, #34472c 0%, #5c7050 30%, #c9ccc6 55%, #a78b62 100%);
  }
  .photo-paintball {
    left: 484px; top: 548px; width: 440px; height: 258px;
    background:
      radial-gradient(circle at 48% 38%, rgba(90,150,255,.9) 0, transparent 70px),
      radial-gradient(circle at 60% 40%, rgba(60,220,120,.8) 0, transparent 30px),
      radial-gradient(circle at 70% 46%, rgba(240,40,60,.85) 0, transparent 40px),
      radial-gradient(circle at 50% 28%, rgba(40,80,230,.6) 0, transparent 140px),
      linear-gradient(150deg, #202a40 0%, #3a2f48 55%, #1e1c1c 100%);
  }
  .photo-cafe {
    left: 484px; top: 800px; width: 436px; height: 154px;
    background:
      radial-gradient(circle at 40% 28%, #ffb347 0, #d96a1e 22px, transparent 60px),
      radial-gradient(ellipse at 60% 95%, #e9e1d4 0, transparent 160px),
      linear-gradient(180deg, #5b4230 0%, #8c6d50 50%, #c8b89e 100%);
  }
  .indoor-panel { left: 36px; top: 818px; width: 435px; height: 297px; }
  .indoor-title { position: absolute; left: 36px; top: 34px; font-family: "Lobster", "Brush Script MT", cursive; font-size: 34px; color: var(--ink); }
  .indoor-list { position: absolute; left: 36px; top: 94px; font-size: 26px; line-height: 38px; color: var(--deep-red); font-weight: 700; white-space: nowrap; }
  .indoor-price { position: absolute; left: 36px; top: 178px; font-size: 25px; }
  .indoor-price .amount { font-size: 34px; font-weight: 700; color: var(--deep-red); }
  .booking-title {
    position: absolute; left: 58px; top: 230px; font-family: "Lobster", "Brush Script MT", cursive; font-size: 44px; color: var(--red);
    transform: rotate(-3deg);
    text-shadow: 2px 2px 0 var(--white), -2px -2px 0 var(--white), 2px -2px 0 var(--white), -2px 2px 0 var(--white), 0 4px 5px rgba(0,0,0,.4);
  }
  .cafe-panel { left: 484px; top: 956px; width: 445px; height: 159px; }
  .cafe-text { position: absolute; left: 26px; top: 4px; font-size: 21px; font-weight: 700; line-height: 34px; white-space: nowrap; }
  .cafe-text .script { font-size: 40px; color: var(--red); }
  .contact-band {
    position: absolute; left: 0; top: 1115px; width: 960px; height: 85px; background: var(--band);
    color: var(--white); padding: 6px 0 0 91px; font-size: 26px; line-height: 38px;
  }
  .contact-band strong { font-weight: 700; }
</style>
</head>
<body>
<main class="poster">
  <div class="backdrop" role="img" aria-label="Rustic wooden backdrop framed with pine garland, pine cones, red baubles and candy canes"></div>

  <div class="header-board" role="img" aria-label="Snow-topped wooden sign board"></div>
  <h1 class="title-main">Christmas</h1>
  <h2 class="title-script">Special Offer</h2>

  <section class="paper offer-panel">
    <p class="line starts">Starts <span class="script">Saturday 20<sup>th</sup> December</span></p>
    <p class="line price"><span class="amount">£10pp</span> – <span class="red">offer includes</span> –</p>
    <p class="line inc-1">Half an hour Toboggan track,</p>
    <p class="line inc-2">Half an hour Slingshot Paintballs <span class="red">(20 paintballs pp)</span></p>
    <p class="line inc-3">Safe Target Archery <span class="red">(indoor ranges)</span></p>
    <p class="line inc-4"><span class="bold">Activities</span> all the family from <span class="red">age 4 to grandparents</span> can join in.</p>
    <p class="line essential script">Booking is Essential</p>
  </section>

  <div class="photo photo-toboggan" role="img" aria-label="Photo of family riding a red sled down a snowy toboggan track"></div>
  <div class="photo photo-paintball" role="img" aria-label="Photo of players aiming slingshot paintball launchers at lit targets in an indoor range"></div>
  <div class="photo photo-cafe" role="img" aria-label="Photo of a cosy cabin café with a wood stove and hot chocolates on a table"></div>

  <section class="paper indoor-panel">
    <p class="indoor-title">Indoor Activities :</p>
    <p class="indoor-list">Mini Curling, Bead Blitz,<br>Safe axe throwing, Air juggler</p>
    <p class="indoor-price">from <span class="amount">£3.5pp</span> &amp; <span class="red">age 6+</span></p>
    <p class="booking-title">For Booking:</p>
  </section>

  <section class="paper cafe-panel">
    <p class="cafe-text"><span class="script">Café</span> open for hot food and drinks<br>in the <span class="red">“Fireside Frost Lodge”</span><br>and the heated<br><span class="red">“Christmas Marquee”</span> &amp; <span class="red">age 4+</span></p>
  </section>

  <footer class="contact-band">
    <p><strong>Message on this post</strong> or <strong>email</strong> at :</p>
    <p>martin@hollowbrookleisurepark.co.uk</p>
  </footer>
</main>
</body>
</html>
```